Law Firm Website Update

I have an existing website but it is very wordy, not very aesthetically pleasing and I want additional features. I would like to update the areas of law and pictures, I would like to add a page for a client to fill in their information and links to other pages. Also want to make it more mobile friendly. site is www.tidemarklegalpc.com

Coding

Coded - Design and coding required

```html
<!DOCTYPE html>
<html lang="en">
<head>
<meta charset="utf-8">
<title>Tidemark Legal P.C.</title>
<link href="https://fonts.googleapis.com/css2?family=Playfair+Display+SC:wght@400;700&family=Poppins:wght@400;500;600&display=swap" rel="stylesheet">
<style>
:root{
  --red:#e2161b;
  --red-dark:#c81015;
  --ink:#1d1d1d;
  --text:#2b2b2b;
  --muted:#555;
  --white:#fff;
  --footer:#efefef;
  --dark:#231f1d;
  --serif:'Playfair Display SC', Georgia, serif;
  --sans:'Poppins', Arial, sans-serif;
}
*{margin:0;padding:0;box-sizing:border-box}
html,body{width:1200px;height:5208px;overflow:hidden}
body{position:relative;background:var(--white);font-family:var(--sans);color:var(--text)}
.abs{position:absolute}
.btn{position:absolute;display:flex;align-items:center;justify-content:center;background:var(--red);color:var(--white);font-family:var(--sans);font-weight:600;font-size:13px;border-radius:4px;letter-spacing:.2px}
.serif-title{font-family:var(--serif);color:var(--red);font-weight:400;line-height:1}
.kicker{font-size:12px;font-weight:500;color:var(--ink);letter-spacing:.3px;display:flex;align-items:center;gap:8px}
.kicker .rule{display:inline-block;width:48px;height:1px;background:var(--ink)}
.photo{position:absolute}

/* brand name (text placeholder for the firm's mark) */
.brand{position:absolute;display:flex;align-items:center;gap:10px;white-space:nowrap;font-family:var(--sans);font-weight:600;color:var(--red);line-height:1}
.brand .mark{display:block;background:var(--red);flex:none}

/* header */
.nav{position:absolute;left:0;top:76px;width:1200px;height:44px;background:var(--red);display:flex;align-items:center}
.nav a{position:absolute;color:var(--white);font-size:12px;font-weight:500;text-decoration:none;white-space:nowrap}

/* hero */
.hero{position:absolute;left:0;top:120px;width:1200px;height:652px;background:linear-gradient(100deg,#1b1714 0%,#3d342c 35%,#2a2420 60%,#4a4038 100%)}
.hero-shade{position:absolute;inset:0;background:rgba(0,0,0,.35)}
.hero h1{position:absolute;left:0;width:1200px;top:110px;text-align:center;font-family:var(--serif);font-weight:400;color:var(--white);font-size:54px;line-height:58px}
.hero p{position:absolute;left:0;width:1200px;top:302px;text-align:center;color:var(--white);font-size:16px;line-height:26px}
.dots{position:absolute;top:602px;left:570px;display:flex;gap:8px}
.dots span{width:7px;height:7px;border-radius:50%;background:#9a9a9a}
.dots span.on{background:var(--white)}

/* about */
.lead{position:absolute;font-size:20px;line-height:32px;color:var(--ink);text-align:justify}
.body-sm{position:absolute;font-size:13px;line-height:26.5px;color:var(--ink);text-align:justify}

/* cards */
.card{position:absolute;top:1596px;width:332px;height:390px;background:var(--white);box-shadow:0 2px 10px rgba(0,0,0,.16);border-radius:3px}
.card .pic{position:absolute;left:8px;top:8px;width:316px;height:206px}
.card .icon{position:absolute;left:140px;top:188px;width:52px;height:52px;border-radius:50%;background:var(--red);border:3px solid var(--white);box-shadow:0 0 0 1px #eee}
.card h3{position:absolute;left:0;width:100%;top:254px;text-align:center;color:var(--red);font-size:19px;font-weight:500;line-height:24px}
.card p{position:absolute;left:20px;right:20px;text-align:center;font-size:13.5px;line-height:25px;color:var(--ink)}

/* dark band */
.band{position:absolute;left:0;top:2196px;width:1200px;height:548px;background:linear-gradient(90deg,#2a2623 0%,#2f2a26 50%,#4a4038 75%,#6a5d52 100%)}
.band h2{position:absolute;left:70px;top:90px;font-family:var(--serif);font-weight:400;color:var(--white);font-size:44px;line-height:56px}
.band p{position:absolute;left:70px;top:290px;width:740px;color:var(--white);font-size:19px;line-height:32px}

/* testimonials */
.reviews{position:absolute;left:0;top:3606px;width:1200px;height:518px;background:var(--red)}
.quote{position:absolute;top:0;width:380px;text-align:center;color:var(--white)}
.quote .avatar{position:absolute;left:144px;top:198px;width:92px;height:92px;border-radius:50%;background:linear-gradient(160deg,#e9e9e9,#9b9b9b);border:3px solid var(--white)}
.quote p{position:absolute;left:0;width:380px;top:308px;font-size:13px;line-height:21.5px}
.quote h4{position:absolute;left:0;width:380px;top:394px;font-family:var(--serif);font-weight:400;font-size:17px}
.quote .stars{position:absolute;left:0;width:380px;top:424px;font-size:11px;letter-spacing:2px;color:#ffd200}

/* contact */
.field{position:absolute;height:46px;border:1px solid #e2e2e2;border-radius:2px;box-shadow:0 1px 4px rgba(0,0,0,.08);font-size:11px;color:#aaa;padding:14px 8px;background:var(--white)}

/* footer */
.footer{position:absolute;left:0;top:4760px;width:1200px;height:448px;background:var(--footer)}
.footer h5{position:absolute;font-family:var(--serif);font-weight:700;font-size:22px;color:var(--ink)}
.footer .underline{position:absolute;width:60px;height:2px;background:var(--red)}
.links li{position:absolute;list-style:none;font-size:15px;color:var(--ink);padding-left:22px}
.links li::before{content:"";position:absolute;left:0;top:8px;width:7px;height:7px;border-radius:50%;background:var(--red)}
.cinfo{position:absolute;font-size:15px;line-height:26px;color:var(--ink)}
.cicon{position:absolute;width:36px;height:36px;border-radius:50%;background:var(--red);display:flex;align-items:center;justify-content:center}
.social{position:absolute;width:38px;height:38px;border-radius:50%;background:var(--red)}
</style>
</head>
<body>

<!-- Header -->
<div class="brand" style="left:88px;top:25px;font-size:22px"><span class="mark" style="width:14px;height:14px"></span>Tidemark Legal PC</div>
<div class="btn" style="left:936px;top:16px;width:202px;height:42px;font-size:13px;font-weight:500">FREE CONSULTATION</div>

<nav class="nav">
  <a style="left:72px">HOME</a>
  <a style="left:178px">ABOUT US</a>
  <a style="left:310px">ATTORNEY PROFILE</a>
  <a style="left:500px">PRACTICE AREAS</a>
  <a style="left:678px">REVIEWS</a>
  <a style="left:792px">PAY ONLINE</a>
  <a style="left:922px">BLOG</a>
  <a style="left:1024px">CONTACT US</a>
</nav>

<!-- Hero -->
<section class="hero" role="img" aria-label="Photo of a lawyer's desk with open book, gavel and coffee cup">
  <div class="hero-shade"></div>
  <h1>Northern California<br>Legal Guidance for<br>Individuals &amp;Businesses</h1>
  <p>Providing clients with sound legal advice, fluid<br>communication &amp; prompt service</p>
  <div class="btn" style="left:469px;top:398px;width:204px;height:64px;font-size:15px;font-weight:500">FREE CONSULTATION</div>
  <div class="dots"><span></span><span></span><span></span><span class="on"></span></div>
</section>

<!-- About -->
<section>
  <h2 class="serif-title abs" style="left:82px;top:884px;font-size:46px">About Us</h2>
  <div class="kicker abs" style="left:82px;top:938px;font-weight:400">WHO WE ARE <span class="rule"></span></div>
  <p class="lead" style="left:82px;top:994px;width:558px">Tidemark Legal P.C. offers a boutique law firm option for clients who want to enjoy all the advantages of big-firm-style representation in a personal and professional environment.</p>
  <p class="body-sm" style="left:82px;top:1130px;width:558px">Out-of-the-box legal strategies that have made the seemingly impossible, possible. Our approach begins with a no-cost consultation to assess our client's needs and evaluate their position in the matter at hand. We strive to meet and exceed our firm mission to provide each and every client with sound legal advice, fluid communication and prompt service.</p>
  <div class="btn" style="left:82px;top:1292px;width:138px;height:46px">KNOW MORE</div>

  <svg class="abs" style="left:900px;top:904px" width="260" height="464" viewBox="0 0 260 464">
    <rect x="6" y="6" width="250" height="452" rx="6" fill="none" stroke="var(--red)" stroke-width="2"/>
    <path d="M214 6 H256 V120 Z" fill="var(--red)"/>
  </svg>
  <div class="photo" role="img" aria-label="Photo of a lawyer in a suit signing papers beside scales and a gavel" style="left:734px;top:926px;width:404px;height:422px;background:linear-gradient(135deg,#cfcfcf 0%,#6e6b67 45%,#3a2a20 100%);border-radius:4px"></div>
</section>

<!-- Practice areas -->
<section>
  <h2 class="serif-title abs" style="left:0;width:1200px;text-align:center;top:1478px;font-size:46px">Practice Areas</h2>
  <div class="kicker abs" style="left:0;width:1200px;justify-content:center;top:1532px"><span class="rule" style="width:30px"></span>WHAT WE DO<span class="rule" style="width:30px"></span></div>

  <div class="card" style="left:70px">
    <div class="pic" role="img" aria-label="Photo of clients meeting with a lawyer at a table" style="background:linear-gradient(135deg,#d8d4cc,#5e5a55 60%,#2f2d2b)"></div>
    <div class="icon"></div>
    <h3>REAL ESTATE</h3>
    <p style="top:292px">Lorem ipsum dolor sit amet, consectetur adipiscing elit, sed do eiusmod tempor</p>
  </div>
  <div class="card" style="left:434px">
    <div class="pic" role="img" aria-label="Photo of two businessmen reviewing a document" style="background:linear-gradient(135deg,#bdbdbd,#6b6b6b 55%,#262626)"></div>
    <div class="icon"></div>
    <h3>COMMERCIAL REAL ESTATE<br>TRANSACTIONS</h3>
    <p style="top:316px">Lorem ipsum dolor sit amet, consectetur adipiscing elit, sed do eiusmod tempor</p>
  </div>
  <div class="card" style="left:798px">
    <div class="pic" role="img" aria-label="Photo of a business meeting with documents and a laptop" style="background:linear-gradient(135deg,#2d3a52,#7b8799 55%,#e6e6e6)"></div>
    <div class="icon"></div>
    <h3>BUSINESS LAW</h3>
    <p style="top:292px">Lorem ipsum dolor sit amet, consectetur adipiscing elit, sed do eiusmod tempor</p>
  </div>

  <div class="btn" style="left:494px;top:2068px;width:212px;height:46px;font-size:12.5px">VIEW ALL OUR SERVICES</div>
</section>

<!-- Experience band -->
<section class="band">
  <div class="photo" role="img" aria-label="Photo of a bronze statue of Lady Justice holding scales" style="left:760px;top:0;width:440px;height:548px;background:linear-gradient(90deg,rgba(47,42,38,0),rgba(120,105,92,.7) 50%,rgba(90,78,68,.9))"></div>
  <h2>Experienced California Attorney<br>Assists with Wide Range of<br>Legal Matters</h2>
  <p>Dedicated Redding law firm handles real estate, business, bankruptcy and litigation issues for individuals and businesses</p>
  <div class="btn" style="left:72px;top:404px;width:212px;height:48px;font-size:15px;font-weight:500">FREE&nbsp; CONSULTING</div>
</section>

<!-- Attorney -->
<section>
  <svg class="abs" style="left:52px;top:2936px" width="420" height="490" viewBox="0 0 420 490">
    <rect x="4" y="8" width="412" height="476" rx="6" fill="none" stroke="var(--red)" stroke-width="2"/>
    <rect x="4" y="370" width="100" height="114" fill="var(--red)"/>
  </svg>
  <div class="photo" role="img" aria-label="Portrait photo of attorney Maren L. Holt" style="left:70px;top:2906px;width:432px;height:506px;background:linear-gradient(180deg,#c2c2c2,#a8a8a8 60%,#2a2a2a);border-radius:3px"></div>

  <h2 class="serif-title abs" style="left:588px;top:2912px;font-size:46px">Maren L. Holt</h2>
  <div class="kicker abs" style="left:588px;top:2972px;font-weight:400">ATTORNEY <span class="rule" style="width:30px"></span></div>
  <p class="lead" style="left:588px;top:3024px;width:558px;font-size:19.5px;line-height:31px">Maren Holt is a California real estate attorney and principal of Tidemark Legal P.C. specializing in corporate law, business law, contract law and real estate law.</p>
  <p class="body-sm" style="left:588px;top:3124px;width:558px">She is also principal and managing broker of Harbor West Properties, a property management and real estate investment company. She holds a degree in Business Administration, Marketing and a Juris Doctorate from the Westbrook University. She formerly served as the Executive Marketing Director and Director of Development for a national trade association.</p>
  <div class="abs" role="img" aria-label="Handwritten signature" style="left:588px;top:3290px;width:236px;height:24px;background:linear-gradient(90deg,rgba(60,60,60,.18),rgba(60,60,60,.06))"></div>
  <div class="abs" style="left:588px;top:3320px;font-size:14px;color:var(--ink)">Tidemark Legal P.C.'s CEO</div>
  <div class="btn" style="left:588px;top:3360px;width:138px;height:46px">KNOW MORE</div>
</section>

<!-- Testimonials -->
<section class="reviews">
  <h2 class="abs" style="left:0;width:1200px;top:80px;text-align:center;font-family:var(--serif);font-weight:400;color:var(--white);font-size:46px">Testimonials</h2>
  <div class="kicker abs" style="left:0;width:1200px;justify-content:center;top:140px;color:var(--white)"><span class="rule" style="width:30px;background:var(--white)"></span>REVIEWS<span class="rule" style="width:30px;background:var(--white)"></span></div>
  <svg class="abs" style="left:104px;top:312px" width="20" height="30" viewBox="0 0 20 30"><path d="M16 2 L4 15 L16 28" fill="none" stroke="var(--white)" stroke-width="2"/></svg>
  <svg class="abs" style="left:1046px;top:312px" width="20" height="30" viewBox="0 0 20 30"><path d="M4 2 L16 15 L4 28" fill="none" stroke="var(--white)" stroke-width="2"/></svg>

  <div class="quote" style="left:182px">
    <div class="avatar" role="img" aria-label="Client portrait photo"></div>
    <p>Lorem ipsum dolor sit amet, consectetur adipiscing elit, sed do eiusmod tempor incididunt ut labore et dolore magna aliqua.</p>
    <h4>JONATHAN SMITH</h4>
    <div class="stars">★★★★★</div>
  </div>
  <div class="quote" style="left:630px">
    <div class="avatar" role="img" aria-label="Client portrait photo"></div>
    <p>Lorem ipsum dolor sit amet, consectetur adipiscing elit, sed do eiusmod tempor incididunt ut labore et dolore magna aliqua.</p>
    <h4>JONATHAN SMITH</h4>
    <div class="stars">★★★★★</div>
  </div>
</section>

<!-- Contact -->
<section>
  <div class="abs" style="left:1032px;top:4124px;width:168px;height:636px;background:#131313"></div>
  <svg class="abs" style="left:774px;top:4212px" width="382" height="150" viewBox="0 0 382 150">
    <rect x="2" y="2" width="378" height="200" fill="none" stroke="var(--red)" stroke-width="2"/>
    <rect x="350" y="2" width="30" height="148" fill="var(--red)"/>
  </svg>
  <div class="photo" role="img" aria-label="Photo of a lawyer in glasses writing at a desk with scales and a gavel" style="left:734px;top:4230px;width:406px;height:430px;background:linear-gradient(160deg,#f4f4f4 0%,#cfcfcf 40%,#3b3b3b 75%,#b9a27a 100%)"></div>

  <h2 class="serif-title abs" style="left:88px;top:4290px;font-size:46px">Contact Us</h2>
  <div class="kicker abs" style="left:92px;top:4346px">GET IN TOUCH <span class="rule" style="width:30px"></span></div>
  <p class="abs" style="left:92px;top:4390px;font-size:13.5px;color:var(--ink)">For more information.Please fill out the following and we will be in touch shortly.</p>

  <div class="field" style="left:92px;top:4448px;width:268px">First Name</div>
  <div class="field" style="left:386px;top:4448px;width:268px">Last Name</div>
  <div class="field" style="left:92px;top:4520px;width:268px">Phone</div>
  <div class="field" style="left:386px;top:4520px;width:268px">Company Name</div>
  <div class="field" style="left:92px;top:4588px;width:562px">Email</div>
  <div class="btn" style="left:92px;top:4660px;width:140px;height:46px;font-size:14px">SUBMIT</div>
</section>

<!-- Footer -->
<footer class="footer">
  <div class="brand" style="left:124px;top:172px;font-size:28px"><span class="mark" style="width:18px;height:18px"></span>Tidemark Legal PC</div>
  <div class="social" aria-label="Social profile" style="left:191px;top:250px"></div>
  <div class="social" aria-label="Social profile" style="left:239px;top:250px"></div>
  <div class="social" aria-label="Social profile" style="left:287px;top:250px"></div>

  <h5 style="left:520px;top:102px">LINKS</h5>
  <div class="underline" style="left:520px;top:140px"></div>
  <ul class="links">
    <li style="left:520px;top:176px">About Us</li>
    <li style="left:520px;top:208px">Attorney Profile</li>
    <li style="left:520px;top:240px">Practice Areas</li>
    <li style="left:520px;top:272px">Reviews</li>
    <li style="left:520px;top:304px">Contact Us</li>
  </ul>

  <h5 style="left:782px;top:102px">CONTACT US</h5>
  <div class="underline" style="left:782px;top:140px"></div>
  <div class="cicon" style="left:782px;top:176px"><svg width="16" height="20" viewBox="0 0 16 20"><path d="M8 1a6 6 0 0 0-6 6c0 5 6 12 6 12s6-7 6-12a6 6 0 0 0-6-6z" fill="#fff"/><circle cx="8" cy="7" r="2.3" fill="var(--red)"/></svg></div>
  <div class="cinfo" style="left:832px;top:170px">2240 Alder Street,<br>Suite B, Redding, California 96001</div>
  <div class="cicon" style="left:782px;top:234px"><svg width="18" height="18" viewBox="0 0 24 24"><path d="M6.6 10.8a15.1 15.1 0 0 0 6.6 6.6l2.2-2.2a1 1 0 0 1 1-.25 11.4 11.4 0 0 0 3.6.57 1 1 0 0 1 1 1V20a1 1 0 0 1-1 1A17 17 0 0 1 3 4a1 1 0 0 1 1-1h3.5a1 1 0 0 1 1 1c0 1.25.2 2.45.57 3.6a1 1 0 0 1-.25 1z" fill="#fff"/></svg></div>
  <div class="cinfo" style="left:832px;top:240px">530-555-0148</div>
  <div class="cicon" style="left:782px;top:286px"><svg width="18" height="14" viewBox="0 0 18 14"><rect x="1" y="1" width="16" height="12" rx="1.5" fill="#fff"/><path d="M1.5 1.8 L9 7.5 L16.5 1.8" fill="none" stroke="var(--red)" stroke-width="1.5"/></svg></div>
  <div class="cinfo" style="left:832px;top:292px">info@tidemarklegalpc.com</div>

  <div class="abs" style="left:56px;top:380px;width:1064px;height:1px;background:var(--red)"></div>
  <p class="abs" style="left:0;width:1200px;top:406px;text-align:center;font-size:13px;color:var(--ink)">Copyright © 2025 All Rights Reserved By Company Name</p>
</footer>

</body>
</html>
```